Winter Fence Sale Fence Types

Please create a flyer, similar to what we did previous, but mimicking this page listing the fence styles: http://brindlepostyards.com/cold-deal-2019

Industry/Entity Type

Residential Construction

Font styles to use
Sans Serif

Colors
cee9f5
33a6d7
d0dfed

Requirements
Must have
• Fence styles and photo of fence styles
Nice to have
• Phone number, address, logo

```html
<!DOCTYPE html>
<html lang="en">
<head>
<meta charset="utf-8">
<title>Winter Fence Sale 2019 – Fence Styles Flyer</title>
<link rel="stylesheet" href="https://fonts.googleapis.com/css2?family=Archivo+Black&family=Roboto:wght@400;500;700&display=swap">
<style>
:root{
  --canvas:#d6d6d6;
  --paper:#ffffff;
  --blue:#3a84c9;
  --blue-bar:rgba(58,132,201,.88);
  --blue-light:#33a6d7;
  --orange:#e38a2c;
  --brown:#54412f;
  --ink:#1f1f1f;
  --overlay:rgba(62,58,52,.78);
  --band:rgba(90,86,80,.82);
  --wood:#c9a66b;
  --wood-light:#ddc08a;
  --leaf:#4e6b34;
  --grass:#6f8f3d;
}
*{box-sizing:border-box;margin:0;padding:0}
html,body{width:1200px;height:3062px;overflow:hidden;background:var(--canvas)}
body{position:relative;font-family:'Roboto',Arial,sans-serif;color:var(--ink)}
.flyer{position:absolute;left:170px;width:860px;background:var(--paper);box-shadow:0 6px 18px rgba(0,0,0,.28);overflow:hidden}
.flyer--front{top:200px;height:1220px}
.flyer--back{top:1620px;height:1214px}
.abs{position:absolute}

/* header */
.brand{left:30px;top:28px;display:flex;gap:14px;align-items:flex-start}
.brand__mark{width:58px;height:58px;background:var(--brown);margin-top:6px}
.brand__name{font-family:'Archivo Black',sans-serif;font-size:24px;color:var(--blue);line-height:1.1}
.brand__phone{font-family:'Archivo Black',sans-serif;font-size:22px;color:var(--ink);line-height:1.2}
.brand__tag{font-size:8px;font-weight:700;margin-top:3px}
.contact{right:62px;top:20px;text-align:right}
.contact__phone{font-size:34px;color:var(--blue);font-weight:500;line-height:1.1}
.contact__addr{font-size:19px;line-height:1.25;margin-top:4px}

/* photos */
.photo{position:absolute;overflow:hidden}
.ph-wood{background:linear-gradient(180deg,#6c7d4a 0%,var(--wood-light) 30%,var(--wood) 75%,#7a8a45 100%)}
.ph-green{background:linear-gradient(180deg,#2f4a26 0%,var(--leaf) 35%,var(--wood) 70%,var(--grass) 100%)}
.ph-house{background:linear-gradient(180deg,#8d8a82 0%,#b49a7a 40%,var(--wood-light) 70%,var(--grass) 100%)}
.ph-dark{background:linear-gradient(180deg,#3d3a33 0%,#7b6042 45%,var(--wood) 75%,#5f7236 100%)}
.ph-red{background:linear-gradient(180deg,#6b7d52 0%,#c98a72 40%,#b8755e 75%,#6f8f3d 100%)}

/* front hero */
.hero{left:0;top:128px;width:860px;height:383px}
.hero__panel{left:111px;top:0;width:637px;height:383px;background:var(--overlay);text-align:center;color:#fff}
.hero__title{font-family:'Archivo Black',sans-serif;font-size:70px;line-height:1;margin-top:80px;letter-spacing:1px}
.hero__sub{font-family:'Archivo Black',sans-serif;font-size:56px;line-height:1;color:var(--orange);margin-top:4px}
.hero__welcome{font-family:'Archivo Black',sans-serif;font-size:23px;margin-top:26px;font-weight:400}
.hero__body{font-size:12.5px;line-height:1.35;margin:20px auto 0;width:540px}
.hl{color:var(--blue-light)}

/* style groups */
.style{position:absolute;width:400px;height:159px}
.style .photo{top:0;height:159px;width:196px}
.style .photo:nth-child(2){left:204px}
.style__label{position:absolute;left:0;bottom:0;width:400px;height:30px;background:var(--blue-bar);color:#fff;font-family:'Archivo Black',sans-serif;font-size:16px;line-height:30px;text-align:center}

/* footer */
.footer{left:0;bottom:0;width:860px;height:82px;background:var(--brown);color:#fff;display:flex;align-items:center;font-size:19px;padding:0 22px}
.footer__item{display:flex;align-items:center;gap:12px;margin-right:48px}
.footer__square{width:22px;height:22px;background:var(--blue);margin-left:28px}
.footer__badge{width:62px;height:52px;background:#f2f2f2;margin-left:20px}
.footer__badge--dark{background:#3b3026;border:2px solid #f2f2f2;width:54px}

/* back */
.back-hero{left:0;top:0;width:860px;height:470px}
.back-band{left:0;top:348px;width:860px;height:122px;background:var(--band);color:#fff;font-family:'Archivo Black',sans-serif;font-size:54px;text-align:center;line-height:122px;letter-spacing:1px}
.price{position:absolute;width:222px;text-align:center}
.price__amt{background:var(--blue);color:#fff;font-family:'Archivo Black',sans-serif;font-size:38px;height:56px;line-height:56px;border-radius:6px 6px 0 0}
.price__lbl{background:var(--brown);color:#fff;font-family:'Archivo Black',sans-serif;font-size:20px;height:36px;line-height:36px;border-radius:0 0 6px 6px}
.price-note{left:281px;top:528px;width:540px;font-size:12.5px;line-height:1.45}
.tile{position:absolute;width:153px;height:163px}
.tile .photo{inset:0}
.tile__label{position:absolute;left:0;bottom:0;width:153px;height:22px;background:var(--blue-bar);color:#fff;font-size:11px;font-weight:500;line-height:22px;text-align:center}
</style>
</head>
<body>

<!-- Front -->
<section class="flyer flyer--front">
  <div class="abs brand">
    <div class="brand__mark"></div>
    <div>
      <div class="brand__name">Brindlepost Yards</div>
      <div class="brand__phone">555-310-4420</div>
      <div class="brand__tag">“Because Good Fences Make Good Neighbors”</div>
    </div>
  </div>
  <div class="abs contact">
    <div class="contact__phone">555-310-4420</div>
    <div class="contact__addr">1180 Harlow Mill Rd,<br>Ashford NC 28000</div>
  </div>

  <div class="abs hero">
    <div class="photo ph-wood" style="inset:0" role="img" aria-label="Photo of a new wooden privacy fence along a lawn"></div>
    <div class="abs hero__panel">
      <div class="hero__title">WINTER</div>
      <div class="hero__sub">FENCE SALE 2019</div>
      <div class="hero__welcome">Welcome to our Winter Fence Sale!</div>
      <p class="hero__body">The fence styles listed below are currently on sale for a limited time at <span class="hl">$12 / FT!</span> Fence styles are <span class="hl">4FT</span> in height, more than several are standard HOA approved fence styles, and will look beautiful in your backyard. Cannot be combined with any other offer.</p>
    </div>
  </div>

  <div class="style" style="left:21px;top:547px">
    <div class="photo ph-wood" role="img" aria-label="Photo of a split rail fence gate"></div>
    <div class="photo ph-green" role="img" aria-label="Photo of a split rail fence in a garden"></div>
    <div class="style__label">2 Rail Split Rail</div>
  </div>
  <div class="style" style="left:435px;top:547px">
    <div class="photo ph-green" role="img" aria-label="Photo of an estate rail fence gate"></div>
    <div class="photo ph-dark" role="img" aria-label="Photo of an estate rail fence with wire"></div>
    <div class="style__label">2 Rail Estate Rail</div>
  </div>
  <div class="style" style="left:21px;top:741px">
    <div class="photo ph-dark" role="img" aria-label="Photo of a dog ear picket fence"></div>
    <div class="photo ph-wood" role="img" aria-label="Photo of a dog ear picket fence beside shrubs"></div>
    <div class="style__label">Dog Ear Picket</div>
  </div>
  <div class="style" style="left:435px;top:741px">
    <div class="photo ph-house" role="img" aria-label="Photo of a French gothic picket fence in front of a house"></div>
    <div class="photo ph-house" role="img" aria-label="Photo of a French gothic picket fence along a yard"></div>
    <div class="style__label">French Gothic Picket</div>
  </div>
  <div class="style" style="left:21px;top:935px">
    <div class="photo ph-dark" role="img" aria-label="Photo of a curved picket fence gate"></div>
    <div class="photo ph-wood" role="img" aria-label="Photo of a curved picket fence along a lawn"></div>
    <div class="style__label">Daybreak Picket</div>
  </div>
  <div class="style" style="left:435px;top:935px">
    <div class="photo ph-green" role="img" aria-label="Photo of a scalloped picket fence by trees"></div>
    <div class="photo ph-wood" role="img" aria-label="Photo of a scalloped picket fence on a lawn"></div>
    <div class="style__label">Sunset Picket</div>
  </div>

  <div class="abs footer">
    <div class="footer__item">
      <svg width="26" height="18" viewBox="0 0 26 18"><rect x="1" y="1" width="24" height="16" fill="none" stroke="#3a84c9" stroke-width="2"/><path d="M1 1l12 9 12-9" fill="none" stroke="#3a84c9" stroke-width="2"/></svg>
      office@brindlepostyards.com
    </div>
    <div class="footer__item">
      <svg width="22" height="22" viewBox="0 0 22 22"><circle cx="11" cy="11" r="9.5" fill="none" stroke="#3a84c9" stroke-width="2"/><ellipse cx="11" cy="11" rx="4" ry="9.5" fill="none" stroke="#3a84c9" stroke-width="1.5"/><path d="M2 11h18" stroke="#3a84c9" stroke-width="1.5"/></svg>
      www.brindlepostyards.com
    </div>
    <div class="footer__square"></div>
    <div class="footer__square" style="margin-left:28px"></div>
  </div>
</section>

<!-- Back -->
<section class="flyer flyer--back">
  <div class="abs back-hero">
    <div class="photo ph-green" style="inset:0" role="img" aria-label="Close-up photo of a wooden picket fence under tree branches"></div>
  </div>
  <div class="abs back-band">WINTER SALE 2019</div>

  <div class="price" style="left:28px;top:504px">
    <div class="price__amt">$14/FT</div>
    <div class="price__lbl">FENCE STYLES</div>
  </div>
  <p class="abs price-note">Choose from our many other fence styles that start at <span class="hl">$14</span> per linear foot! These styles can be up to <span class="hl">6FT</span> in height.</p>

  <div class="tile" style="left:28px;top:631px"><div class="photo ph-wood" role="img" aria-label="Photo of a dog ear privacy fence"></div><div class="tile__label">Dog Ear Privacy</div></div>
  <div class="tile" style="left:189px;top:631px"><div class="photo ph-house" role="img" aria-label="Photo of an arched privacy fence"></div><div class="tile__label">Daybreak Privacy</div></div>
  <div class="tile" style="left:350px;top:631px"><div class="photo ph-wood" role="img" aria-label="Photo of a scalloped privacy fence"></div><div class="tile__label">Sunset Privacy</div></div>
  <div class="tile" style="left:511px;top:631px"><div class="photo ph-green" role="img" aria-label="Photo of a three rail estate fence with wire"></div><div class="tile__label">3 Rail Estate Rail with wire</div></div>
  <div class="tile" style="left:672px;top:631px"><div class="photo ph-dark" role="img" aria-label="Photo of an arched privacy fence with rail"></div><div class="tile__label">Daybreak Privacy</div></div>

  <div class="price" style="left:312px;top:822px">
    <div class="price__amt">$16/FT</div>
    <div class="price__lbl">FENCE STYLES</div>
  </div>

  <div class="tile" style="left:28px;top:933px"><div class="photo ph-red" role="img" aria-label="Photo of a four rail fence with wire beside a house"></div><div class="tile__label">4 Rail Estate Rail with Wire</div></div>
  <div class="tile" style="left:189px;top:933px"><div class="photo ph-dark" role="img" aria-label="Photo of a stained shadowbox fence"></div><div class="tile__label">Shadowbox</div></div>
  <div class="tile" style="left:350px;top:933px"><div class="photo ph-red" role="img" aria-label="Photo of an arched shadowbox fence"></div><div class="tile__label">Daybreak Shadowbox</div></div>
  <div class="tile" style="left:511px;top:933px"><div class="photo ph-green" role="img" aria-label="Photo of a scalloped shadowbox fence"></div><div class="tile__label">Sunset Shadowbox</div></div>
  <div class="tile" style="left:672px;top:933px"><div class="photo ph-house" role="img" aria-label="Photo of a top cap privacy fence"></div><div class="tile__label">Top Cap</div></div>

  <div class="abs footer" style="height:76px">
    <div class="footer__item" style="margin-right:28px">
      <svg width="26" height="18" viewBox="0 0 26 18"><rect x="1" y="1" width="24" height="16" fill="none" stroke="#3a84c9" stroke-width="2"/><path d="M1 1l12 9 12-9" fill="none" stroke="#3a84c9" stroke-width="2"/></svg>
      office@brindlepostyards.com
    </div>
    <div class="footer__item" style="margin-right:20px">
      <svg width="22" height="22" viewBox="0 0 22 22"><circle cx="11" cy="11" r="9.5" fill="none" stroke="#3a84c9" stroke-width="2"/><ellipse cx="11" cy="11" rx="4" ry="9.5" fill="none" stroke="#3a84c9" stroke-width="1.5"/><path d="M2 11h18" stroke="#3a84c9" stroke-width="1.5"/></svg>
      www.brindlepostyards.com
    </div>
    <div class="footer__badge footer__badge--dark" style="margin-left:auto"></div>
    <div class="footer__badge" style="margin-right:30px"></div>
  </div>
</section>

</body>
</html>
```